Quillmere Financial Plans

I am looking for a complete resdesign of my small financial presentation. This is a Word Doc/PDF that I print off when meeting with people in private. I often present my "two pager" that I have been using for years and years. It tells them the basics of what I do, how I help people and foundational financial principles.

I have recently gone out on my own in business and have completely rebranded. This presentation is my most used tool, so it is the first of many things I would like to redo. I am hoping it will somehow coordinate with the colors of my business, not necessarily the EXACT same 3 colors everywhere, but have the design colors compliment.

I've uploaded all my logo designs, as well as the current "two-pager". I am not against it going to 3 pages if needed. As it will still land on 2 pages with duplex printing.

It has always been VERY simple. I am wanting it built into a more professional and design specific format, to show off my branding, without being over cluttered.

I am completely open to ANY graphics changes. Obviously some are very novice, the house on the last page has always been overly simplified.

```html
<!DOCTYPE html>
<html lang="en">
<head>
<meta charset="utf-8">
<title>Quillmere Financial Plans – Two Pager</title>
<link href="https://fonts.googleapis.com/css2?family=Montserrat:wght@400;500;600;700;800&display=swap" rel="stylesheet">
<style>
:root{
  --navy:#0f2233;
  --navy-2:#1b3246;
  --green:#1fb040;
  --green-bright:#2ccf4c;
  --mint:#c8f4d2;
  --grey-bg:#ebebeb;
  --grey-soft:#f1f1f1;
  --grey-mid:#c9cccf;
  --grey-dark:#8a8f96;
  --red:#e11d25;
  --white:#ffffff;
}
*{box-sizing:border-box;margin:0;padding:0}
html,body{width:1200px;height:2401px;overflow:hidden}
body{background:var(--grey-bg);font-family:'Montserrat',sans-serif;color:var(--navy);position:relative}
.page{position:absolute;left:220px;width:762px;height:1100px;background:var(--white);box-shadow:0 2px 8px rgba(0,0,0,.08);overflow:hidden}
.page-one{top:68px}
.page-two{top:1230px}
.abs{position:absolute}
.brand{left:50px;top:36px;font-size:17px;font-weight:700;color:var(--navy);letter-spacing:.4px;white-space:nowrap}
.corner-pattern{right:0;top:0;width:160px;height:130px;background:linear-gradient(225deg,rgba(31,176,64,.35),rgba(200,204,208,.25) 45%,rgba(255,255,255,0) 75%)}
.h-title{font-size:26px;font-weight:800;line-height:27px;letter-spacing:.2px}
.h-title .accent{color:var(--green)}
/* challenge cards */
.card{left:50px;width:246px;border-radius:14px;background:linear-gradient(160deg,#2c4256,#122536 70%);color:var(--white);padding:14px 16px 0 19px;overflow:hidden}
.card-head{display:flex;align-items:center;gap:8px;margin-bottom:8px}
.card-icon{width:44px;height:44px;border-radius:50%;background:var(--white);border:2px dashed var(--green);display:flex;align-items:center;justify-content:center}
.card-title{font-size:20px;font-weight:700;letter-spacing:.3px}
.card p{font-size:12.2px;line-height:14.4px;font-weight:400;letter-spacing:-.15px}
.card b{font-weight:700}
.source{display:inline-block;background:var(--green);color:var(--white);font-size:9.5px;font-weight:700;border-radius:10px;padding:3px 10px;margin:4px 0 12px}
/* facing icons */
.step{width:150px;text-align:center;margin-left:-75px}
.ring{width:68px;height:68px;border-radius:50%;border:1.5px dashed var(--navy);display:flex;align-items:center;justify-content:center;margin:0 auto}
.ring-core{width:58px;height:58px;border-radius:50%;background:var(--navy);border:3px solid var(--green);display:flex;align-items:center;justify-content:center}
.step-title{font-size:15.5px;font-weight:800;line-height:17px;margin-top:8px}
.step-sub{font-size:13.5px;font-weight:400;line-height:17px;letter-spacing:.3px}
.chev{color:var(--green-bright);font-size:14px;font-weight:800;line-height:14px;display:block}
.small-sub{font-size:12.5px;line-height:14px}
/* how section */
.pill{left:522px;width:198px;height:44px;background:var(--mint);border-radius:4px;display:flex;align-items:center;gap:8px;padding-left:10px;font-size:10.5px;font-weight:700}
.pill-arrow{position:absolute;right:-2px;top:0}
.pointer{left:505px;font-size:13px;font-weight:800;color:var(--navy)}
.partner{width:96px;height:35px;border-radius:4px;background:#f0f1f2;display:flex;align-items:center;justify-content:center;font-size:10px;font-weight:600;color:var(--navy-2);text-align:center;line-height:11px}
.brace{left:315px;top:1014px;width:406px;height:8px;border:2px solid var(--navy);border-top:none;border-radius:0 0 4px 4px}
.pay-us{left:315px;width:406px;top:1030px;text-align:center;font-size:13px;font-weight:800}
.footer-bar{left:0;bottom:0;width:762px;height:35px;background:linear-gradient(90deg,#0d1f2e 40%,#0f3a2a 70%,var(--green) 100%);display:flex;align-items:center;justify-content:flex-end;gap:10px;padding-right:22px;color:var(--white);font-size:11.5px;font-weight:500}
.page-num{width:20px;height:20px;border-radius:50%;border:1.5px solid var(--white);font-size:10px;display:flex;align-items:center;justify-content:center}
/* page two */
.rule-band{left:0;top:0;width:762px;height:460px;background:var(--grey-soft)}
.rate-table{width:160px;font-size:14px}
.rate-head{display:flex;height:43px;color:var(--white);font-size:17px;font-weight:700}
.rate-head .age{width:80px;background:var(--navy);display:flex;align-items:center;justify-content:center}
.rate-head .rate{flex:1;background:var(--green);display:flex;align-items:center;justify-content:center}
.rate-row{display:flex;height:32px;align-items:center;border-bottom:1.2px solid #9aa0a6}
.rate-row .age{width:80px;text-align:center}
.rate-row .amt{flex:1;text-align:center}
.first-col .age{font-weight:700}
.doubles{display:flex;align-items:center;gap:12px}
.doubles-text{line-height:14px}
.doubles-text .m{font-size:12.5px;font-weight:800}
.doubles-text .e{font-size:16.5px;font-weight:800;color:var(--green-bright);line-height:16px}
.pillar{top:645px;width:142px}
.pillar-head{height:85px;border-radius:10px 10px 0 0;display:flex;flex-direction:column;align-items:center;justify-content:center;gap:6px;color:var(--white);font-size:15px;font-weight:700}
.pillar-head.navy{background:var(--navy)}
.pillar-head.green{background:var(--green)}
.pillar-badge{width:42px;height:42px;border-radius:50%;border:1.5px dashed var(--white);display:flex;align-items:center;justify-content:center}
.pillar-body{height:145px;background:#eeeeee;border-radius:0 0 10px 10px;text-align:center;font-size:11.3px;font-weight:700;line-height:15.5px;padding-top:18px}
.pillar-body p{margin-bottom:9px}
.pillar-cap{width:96px;height:35px;background:#d3d5d8;color:var(--red);font-size:14px;font-weight:800;display:flex;align-items:center;justify-content:center}
.foundation{left:83px;top:945px;width:592px;height:70px;border-radius:12px;background:var(--grey-dark);color:var(--white);font-size:12.3px;font-weight:700}
.found-col{position:absolute;top:10px;text-align:center}
.found-col span{display:block;padding:4px 0}
.found-col span:first-child{border-bottom:1.2px solid #e6e6e6}
.fund-stand{left:598px;top:510px;display:flex;align-items:center;gap:6px;font-size:21px;font-weight:800;color:var(--navy)}
.fund-stand i{width:30px;height:30px;border-radius:50%;border:4px solid var(--red);display:block}
</style>
</head>
<body>

<!-- PAGE ONE -->
<section class="page page-one">
  <div class="abs corner-pattern" role="img" aria-label="Decorative triangle pattern in green and grey"></div>
  <div class="abs brand">QUILLMERE FINANCIAL PLANS</div>

  <h1 class="abs h-title" style="left:50px;top:90px">THE FINANCIAL<br><span class="accent">CHALLENGE</span></h1>
  <h2 class="abs h-title" style="left:315px;top:90px">FACING<br><span class="accent">THE CHALLENGE</span></h2>

  <article class="abs card" style="top:157px;height:266px" role="img" aria-label="Savings card over a dark photo of hands with coins">
    <div class="card-head"><div class="card-icon"><svg width="22" height="22" viewBox="0 0 24 24" fill="none" stroke="#0f2233" stroke-width="1.6"><circle cx="12" cy="12" r="8"/><path d="M12 7v10M9.5 9.5h4a1.5 1.5 0 010 3h-3a1.5 1.5 0 000 3h4"/></svg></div><div class="card-title">SAVINGS</div></div>
    <p><b>49%</b> of canadian employees are living paycheque to paycheque. <b>25%</b> of canadians are unable to cover an unexpected <b>$500</b> expense</p>
    <span class="source">National Data Office (feb 2023)</span>
    <p><b>25%</b> of canadians need to access their retirement savings early. <b>20%</b> of canadians have no savings. 39% of canadians aged 55-65 have less than <b>$5,000</b> in savings.</p>
    <span class="source">Federal Finance Bureau (june 2023)</span>
  </article>

  <article class="abs card" style="top:435px;height:268px" role="img" aria-label="Debt card over a dark photo of banknotes">
    <div class="card-head"><div class="card-icon"><svg width="22" height="22" viewBox="0 0 24 24" fill="none" stroke="#0f2233" stroke-width="1.6"><rect x="3" y="7" width="18" height="11" rx="2"/><path d="M3 11h18"/></svg></div><div class="card-title">DEBT</div></div>
    <p>The average canadian has <b>$22,131</b> in consumer debt. Which excludes mortgages.</p>
    <span class="source">Halvern Reports (aug 2024)</span>
    <p>Over <b>55%</b> of canadians hold credit card debt and the total canadian household debt has increased to <b>$2.52trillion</b>, including consumer credit, mortgage and non-mortgage loans.</p>
    <span class="source">National Lenders Assoc. (aug 2024)</span>
  </article>

  <article class="abs card" style="top:716px;height:291px" role="img" aria-label="Insurance card over a dark photo of a family meeting">
    <div class="card-head"><div class="card-icon"><svg width="22" height="22" viewBox="0 0 24 24" fill="none" stroke="#0f2233" stroke-width="1.6"><path d="M12 3l7 3v5c0 5-3 8-7 10-4-2-7-5-7-10V6z"/></svg></div><div class="card-title">INSURANCE</div></div>
    <p><b>45%</b> of canadians do not have individual life insurance coverage, but <b>48%</b> say their families would face financial trouble within 6 months of losing someone.</p>
    <span class="source">Pennock Research Intl. (apr 2023)</span>
    <p>2-in-5 canadians (<b>43%</b> women / <b>44%</b> men) will be diagosed with a form of cancer or other critical illness during their lifetime. Every 7 seconds.</p>
    <span class="source">Public Health Data (june 2024)</span>
  </article>

  <!-- facing the challenge -->
  <div class="abs step" style="left:365px;top:168px">
    <div class="ring"><div class="ring-core"><svg width="28" height="28" viewBox="0 0 24 24" fill="none" stroke="#fff" stroke-width="1.5"><rect x="4" y="6" width="16" height="9" rx="1" transform="rotate(-12 12 10)"/><rect x="4" y="10" width="16" height="9" rx="1"/></svg></div></div>
    <div class="step-title">CASH<br>FLOW</div>
    <div class="step-sub" style="margin-top:6px">ANALYSZE</div>
    <div class="step-sub" style="margin-top:34px;font-size:12.5px">FREE UP</div>
  </div>
  <div class="abs" style="left:430px;top:156px;width:36px;font-size:12.5px;line-height:14px;text-align:center">$400<br>$600<span class="chev" style="margin-top:4px">&#x276F;</span></div>

  <div class="abs step" style="left:522px;top:168px">
    <div class="ring"><div class="ring-core"><svg width="28" height="28" viewBox="0 0 24 24" fill="none" stroke="#fff" stroke-width="1.5"><path d="M3 12a9 9 0 0118 0zM12 12v6a2 2 0 01-4 0"/></svg></div></div>
    <div class="step-title">CASH FLOW<br>PROTECTION</div>
    <div class="step-sub" style="margin-top:6px">INCOME<br>PROTECTION</div>
    <div style="display:flex;justify-content:center;gap:60px;margin-top:2px"><span class="chev">&#x2335;</span><span class="chev">&#x2335;</span></div>
    <div style="display:flex;justify-content:center;gap:12px;margin-top:2px" class="small-sub"><span>Life<br>Insurance</span><span>CI/DI<br>Insurance</span></div>
  </div>

  <div class="abs step" style="left:667px;top:168px">
    <div class="ring"><div class="ring-core"><svg width="28" height="28" viewBox="0 0 24 24" fill="none" stroke="#fff" stroke-width="1.5"><rect x="3" y="8" width="15" height="10" rx="1.5"/><path d="M3 12h15"/><circle cx="18" cy="14" r="3"/></svg></div></div>
    <div class="step-title">DEBT<br>MANAGEMENT</div>
    <div class="step-sub" style="margin-top:6px">20%</div>
    <span class="chev" style="margin-top:4px">&#x2335;</span>
    <div class="step-sub" style="margin-top:10px">6%-7%</div>
  </div>

  <div class="abs step" style="left:365px;top:378px">
    <div class="ring"><div class="ring-core"><svg width="28" height="28" viewBox="0 0 24 24" fill="none" stroke="#fff" stroke-width="1.5"><rect x="3" y="8" width="18" height="11" rx="1.5"/><path d="M12 10v7M8.5 13.5h7"/></svg></div></div>
    <div class="step-title">EMERGENCY<br>FUND</div>
    <div class="step-sub" style="margin-top:6px">IF/ WHEN</div>
    <span class="chev" style="margin-top:4px">&#x2335;</span>
    <div class="step-sub" style="margin-top:6px">3/6<br>Months</div>
  </div>

  <div class="abs step" style="left:522px;top:378px">
    <div class="ring"><div class="ring-core"><svg width="28" height="28" viewBox="0 0 24 24" fill="none" stroke="#fff" stroke-width="1.5"><circle cx="12" cy="8" r="4"/><path d="M12 6v4M5 20c1-4 4-6 7-6s6 2 7 6"/></svg></div></div>
    <div class="step-title">BUILD<br>WEALTH</div>
    <div class="step-sub" style="margin-top:6px">FINANCIAL<br>INDEPENDENCE<br>NUMBER<br>(F.I.N)</div>
    <svg width="36" height="32" viewBox="0 0 36 32" fill="none" stroke="#0f2233" stroke-width="1.6" style="margin-top:4px"><path d="M4 12a14 8 0 0128 0v16H4z"/><path d="M4 14h28M16 14h4v6h-4z"/></svg>
  </div>

  <div class="abs step" style="left:667px;top:378px">
    <div class="ring"><div class="ring-core"><svg width="28" height="28" viewBox="0 0 24 24" fill="none" stroke="#fff" stroke-width="1.5"><rect x="4" y="4" width="16" height="16" rx="1.5"/><rect x="7" y="7" width="10" height="10"/><path d="M12 9v6"/></svg></div></div>
    <div class="step-title">RESERVE<br>WEALTH</div>
    <div class="step-sub" style="margin-top:6px">LEAVING<br>A LEGACY</div>
    <div class="step-sub" style="margin-top:18px">Will Prep</div>
  </div>

  <h2 class="abs h-title" style="left:315px;top:632px;font-size:25px">HOW WE WILL DO IT</h2>

  <svg class="abs" style="left:313px;top:684px" width="184" height="184" viewBox="-1 -1 184 184" role="img" aria-label="Pie chart: living expenses, taxes, savings, debt">
    <g stroke="#fff" stroke-width="3">
      <path d="M91 91L91 0A91 91 0 0 0 91 182Z" fill="#0f2233"/>
      <path d="M91 91L91 0A91 91 0 0 1 178.9 67.4Z" fill="#0f2233"/>
      <path d="M91 91L178.9 67.4A91 91 0 0 1 178.9 114.6Z" fill="#c8f4d2"/>
      <path d="M91 91L178.9 114.6A91 91 0 0 1 91 182Z" fill="#1fb040"/>
    </g>
    <g font-family="Montserrat,sans-serif" font-weight="700" font-size="11.5" fill="#fff" text-anchor="middle">
      <text x="48" y="114">Living</text><text x="48" y="130">Expenses</text>
      <text x="120" y="59">Taxes</text>
      <text x="150" y="96" fill="#0f2233" font-size="11">SAVINGS</text>
      <text x="120" y="158">Debt</text>
    </g>
  </svg>

  <span class="abs pointer" style="top:692px">&#x276F;</span>
  <span class="abs pointer" style="top:741px">&#x276F;</span>
  <span class="abs pointer" style="top:790px">&#x276F;</span>
  <span class="abs pointer" style="top:839px">&#x276F;</span>
  <div class="abs pill" style="top:682px"><svg width="22" height="22" viewBox="0 0 24 24" fill="none" stroke="#0f2233" stroke-width="1.5"><circle cx="9" cy="5" r="2.5"/><path d="M9 8v8M9 16l-3 5M9 16l3 5M14 12h6v9h-6z"/></svg>RETIREMENT SAVINGS<svg class="pill-arrow" width="14" height="44" viewBox="0 0 14 44"><path d="M2 0L12 22L2 44" fill="none" stroke="#2ccf4c" stroke-width="4"/></svg></div>
  <div class="abs pill" style="top:731px"><svg width="22" height="22" viewBox="0 0 24 24" fill="none" stroke="#0f2233" stroke-width="1.5"><circle cx="12" cy="8" r="4"/><path d="M5 21c1-5 4-7 7-7s6 2 7 7M7 5l5-3 5 3"/></svg>CHILDRREN'S EDUCATION<svg class="pill-arrow" width="14" height="44" viewBox="0 0 14 44"><path d="M2 0L12 22L2 44" fill="none" stroke="#2ccf4c" stroke-width="4"/></svg></div>
  <div class="abs pill" style="top:780px"><svg width="22" height="22" viewBox="0 0 24 24" fill="none" stroke="#0f2233" stroke-width="1.5"><path d="M12 3l7 3v5c0 5-3 8-7 10-4-2-7-5-7-10V6z"/><path d="M9 12l2 2 4-4"/></svg>PROPER PROTECTION<svg class="pill-arrow" width="14" height="44" viewBox="0 0 14 44"><path d="M2 0L12 22L2 44" fill="none" stroke="#2ccf4c" stroke-width="4"/></svg></div>
  <div class="abs pill" style="top:829px"><svg width="22" height="22" viewBox="0 0 24 24" fill="none" stroke="#0f2233" stroke-width="1.5"><rect x="5" y="10" width="14" height="11" rx="1"/><path d="M8 10V7a4 4 0 017-2"/></svg>FREEDOM FROM DEBT<svg class="pill-arrow" width="14" height="44" viewBox="0 0 14 44"><path d="M2 0L12 22L2 44" fill="none" stroke="#2ccf4c" stroke-width="4"/></svg></div>

  <div class="abs partner" style="left:316px;top:887px">Tallpine Assurance</div>
  <div class="abs partner" style="left:419px;top:887px">Corvel Mutual</div>
  <div class="abs partner" style="left:521px;top:887px">Brightwater Group</div>
  <div class="abs partner" style="left:624px;top:887px">Halden Partners</div>
  <div class="abs partner" style="left:316px;top:927px">Orchard Benefit</div>
  <div class="abs partner" style="left:419px;top:927px">Pellham Cover</div>
  <div class="abs partner" style="left:521px;top:927px">Westmark</div>
  <div class="abs partner" style="left:624px;top:927px">Drayton Mutual</div>
  <div class="abs partner" style="left:367px;top:972px">Fieldpath Invest</div>
  <div class="abs partner" style="left:470px;top:972px">Kestrel Life</div>
  <div class="abs partner" style="left:574px;top:972px">Sorrento</div>

  <div class="abs brace"></div>
  <div class="abs pay-us">PAY US</div>

  <div class="abs footer-bar">©QUILLMERE | FINANCIAL PLANS <span class="page-num">1</span></div>
</section>

<!-- PAGE TWO -->
<section class="page page-two">
  <div class="abs rule-band"></div>
  <div class="abs corner-pattern" role="img" aria-label="Decorative triangle pattern in green and grey"></div>
  <div class="abs brand">QUILLMERE FINANCIAL PLANS</div>

  <h2 class="abs h-title" style="left:50px;top:104px">RULE OF 72</h2>

  <div class="abs rate-table first-col" style="left:48px;top:141px">
    <div class="rate-head"><div class="age">AGE</div><div class="rate">4%</div></div>
    <div class="rate-row"><span class="age">29</span><span class="amt">$10,000</span></div>
    <div class="rate-row"><span class="age">47</span><span class="amt">$20,000</span></div>
    <div class="rate-row"><span class="age">65</span><span class="amt">$40,000</span></div>
  </div>
  <div class="abs rate-table" style="left:214px;top:141px">
    <div class="rate-head"><div class="age">AGE</div><div class="rate">6%</div></div>
    <div class="rate-row"><span class="age">29</span><span class="amt">$10,000</span></div>
    <div class="rate-row"><span class="age">41</span><span class="amt">$20,000</span></div>
    <div class="rate-row"><span class="age">53</span><span class="amt">$40,000</span></div>
    <div class="rate-row"><span class="age">65</span><span class="amt">$80,000</span></div>
  </div>
  <div class="abs rate-table" style="left:380px;top:141px">
    <div class="rate-head"><div class="age">AGE</div><div class="rate">8%</div></div>
    <div class="rate-row"><span class="age">29</span><span class="amt">$10,000</span></div>
    <div class="rate-row"><span class="age">38</span><span class="amt">$20,000</span></div>
    <div class="rate-row"><span class="age">47</span><span class="amt">$40,000</span></div>
    <div class="rate-row"><span class="age">56</span><span class="amt">$80,000</span></div>
    <div class="rate-row"><span class="age">65</span><span class="amt">$160,000</span></div>
  </div>
  <div class="abs rate-table" style="left:546px;top:141px">
    <div class="rate-head"><div class="age">AGE</div><div class="rate">12%</div></div>
    <div class="rate-row"><span class="age">29</span><span class="amt">$10,000</span></div>
    <div class="rate-row"><span class="age">35</span><span class="amt">$20,000</span></div>
    <div class="rate-row"><span class="age">41</span><span class="amt">$40,000</span></div>
    <div class="rate-row"><span class="age">47</span><span class="amt">$80,000</span></div>
    <div class="rate-row"><span class="age">53</span><span class="amt">$160,000</span></div>
    <div class="rate-row"><span class="age">59</span><span class="amt">$320,000</span></div>
  </div>

  <div class="abs doubles" style="left:64px;top:392px"><svg width="46" height="36" viewBox="0 0 46 36" fill="none" stroke="#0f2233" stroke-width="1.5"><rect x="2" y="8" width="28" height="16" rx="2"/><circle cx="16" cy="16" r="4"/><path d="M32 34c-6 0-9-3-9-8s4-9 9-12c5 3 9 7 9 12s-3 8-9 8z" stroke="#1fb040"/></svg><div class="doubles-text"><div class="m">MONEY<br>DOUBLES</div><div class="e">EVERY<br>18 YEARS</div></div></div>
  <div class="abs doubles" style="left:232px;top:392px"><svg width="46" height="36" viewBox="0 0 46 36" fill="none" stroke="#0f2233" stroke-width="1.5"><rect x="2" y="8" width="28" height="16" rx="2"/><circle cx="16" cy="16" r="4"/><path d="M32 34c-6 0-9-3-9-8s4-9 9-12c5 3 9 7 9 12s-3 8-9 8z" stroke="#1fb040"/></svg><div class="doubles-text"><div class="m">MONEY<br>DOUBLES</div><div class="e">EVERY<br>12 YEARS</div></div></div>
  <div class="abs doubles" style="left:398px;top:392px"><svg width="46" height="36" viewBox="0 0 46 36" fill="none" stroke="#0f2233" stroke-width="1.5"><rect x="2" y="8" width="28" height="16" rx="2"/><circle cx="16" cy="16" r="4"/><path d="M32 34c-6 0-9-3-9-8s4-9 9-12c5 3 9 7 9 12s-3 8-9 8z" stroke="#1fb040"/></svg><div class="doubles-text"><div class="m">MONEY<br>DOUBLES</div><div class="e">EVERY<br>9 YEARS</div></div></div>
  <div class="abs doubles" style="left:563px;top:392px"><svg width="46" height="36" viewBox="0 0 46 36" fill="none" stroke="#0f2233" stroke-width="1.5"><rect x="2" y="8" width="28" height="16" rx="2"/><circle cx="16" cy="16" r="4"/><path d="M32 34c-6 0-9-3-9-8s4-9 9-12c5 3 9 7 9 12s-3 8-9 8z" stroke="#1fb040"/></svg><div class="doubles-text"><div class="m">MONEY<br>DOUBLES</div><div class="e">EVERY<br>6 YEARS</div></div></div>

  <h2 class="abs h-title" style="left:50px;top:488px">STRUCTURE</h2>
  <div class="abs fund-stand">PitchPool<i></i></div>

  <svg class="abs" style="left:0;top:520px" width="762" height="120" viewBox="0 0 762 120" role="img" aria-label="Roof and beam of the financial structure">
    <polygon points="110,50 380,7 650,50" fill="#b4b9be"/>
    <rect x="48" y="50" width="662" height="10" fill="#cfd2d6"/>
    <rect x="83" y="70" width="592" height="20" fill="#e2e3e5"/>
    <rect x="95" y="98" width="96" height="12" fill="#c3c6c9"/>
    <rect x="252" y="98" width="96" height="12" fill="#c3c6c9"/>
    <rect x="409" y="98" width="96" height="12" fill="#c3c6c9"/>
    <rect x="567" y="98" width="96" height="12" fill="#c3c6c9"/>
  </svg>

  <div class="abs pillar" style="left:72px">
    <div class="pillar-head navy"><div class="pillar-badge"><svg width="22" height="22" viewBox="0 0 24 24" fill="none" stroke="#fff" stroke-width="1.6"><path d="M4 11l8-7 8 7v9H4z"/><path d="M10 20v-5h4v5"/></svg></div>HOME</div>
    <div class="pillar-body"><p>PARTNER WITH<br>MORTGAGE<br>BROKERS FOR<br>BEST RATES</p><p>MORTGAGE<br>INSURANCE<br>ALTERNATIVES</p></div>
  </div>
  <div class="abs pillar" style="left:229px">
    <div class="pillar-head green"><div class="pillar-badge"><svg width="22" height="22" viewBox="0 0 24 24" fill="none" stroke="#fff" stroke-width="1.6"><circle cx="12" cy="12" r="7"/><path d="M12 8v8"/></svg></div>RRSP</div>
    <div class="pillar-body"><p>TAX DEDUCTION</p><p>TAX DEFERRED</p></div>
  </div>
  <div class="abs pillar" style="left:386px">
    <div class="pillar-head navy"><div class="pillar-badge"><svg width="22" height="22" viewBox="0 0 24 24" fill="none" stroke="#fff" stroke-width="1.6"><path d="M4 10l8-5 8 5M6 10v8M12 10v8M18 10v8M4 20h16"/></svg></div>TFSA</div>
    <div class="pillar-body"><p>NO TAX<br>DEDUCTIONS</p><p>TAX FREE<br>GROWTH</p><p>2009-$102,000</p><p>2025 LIMIT -<br>$7000/YR</p></div>
  </div>
  <div class="abs pillar" style="left:544px">
    <div class="pillar-head green"><div class="pillar-badge"><svg width="22" height="22" viewBox="0 0 24 24" fill="none" stroke="#fff" stroke-width="1.6"><path d="M3 12a9 9 0 0118 0zM12 12v7"/></svg></div>PERM LIFE</div>
    <div class="pillar-body"><p>NO TAX<br>DEDUCTION</p><p>QUALIFY</p><p>TAX DEFERRED<br>GROWTH</p></div>
  </div>

  <div class="abs pillar-cap" style="left:95px;top:890px">SELL</div>
  <div class="abs pillar-cap" style="left:252px;top:890px">100% TAX</div>
  <div class="abs pillar-cap" style="left:409px;top:890px">0% TAX</div>
  <div class="abs pillar-cap" style="left:567px;top:890px">0% TAX</div>
  <div class="abs" style="left:83px;top:928px;width:120px;height:8px;background:#c3c6c9"></div>
  <div class="abs" style="left:240px;top:928px;width:120px;height:8px;background:#c3c6c9"></div>
  <div class="abs" style="left:397px;top:928px;width:120px;height:8px;background:#c3c6c9"></div>
  <div class="abs" style="left:555px;top:928px;width:120px;height:8px;background:#c3c6c9"></div>

  <div class="abs foundation">
    <div class="found-col" style="left:60px;width:240px"><span>EMERGENCY/OPPORTUNITY FUNDS</span><span>CASHFLOW PROTECTION (LI/CI/DI)</span></div>
    <div class="found-col" style="left:338px;width:200px"><span>DEBT MANAGEMENT</span><span>CASH FLOW</span></div>
  </div>

  <div class="abs footer-bar">©QUILLMERE | FINANCIAL PLANS <span class="page-num">2</span></div>
</section>

</body>
</html>
```